High-end residential home builder needs a business card design

We need a new business card design for a small residential construction company based in Boise, Idaho. We specialize in building custom high-end homes and remodels, with a focus on great design and craftsmanship.

We would like to use our current logo, but open to new color suggestions.
Just looking for a clean, sharp, modern design that looks high-end.

Target Market(s)

Upscale clientele

Industry/Entity Type

Contractor

Contact Information for Business Card

Company: Stonehaven Custom Builders
Name: Colin Marsh
Phone number: 208 637 4120
Email: ColinMarshSCB@quillpost.net
Website: Stonehavencustombuilders.com

Font styles to use
Serif
Sans Serif

Requirements
Must have
• Company Logo
Company name
My name
My phone number
My email
Company website
Nice to have
• I have attached a few photos of cards that I really like.

```html
<!DOCTYPE html>
<html lang="en">
<head>
<meta charset="utf-8">
<title>Stonehaven Custom Builders – Business Card</title>
<link href="https://fonts.googleapis.com/css2?family=Montserrat:wght@600&family=Roboto:wght@400;500&display=swap" rel="stylesheet">
<style>
  :root {
    --page: #efece7;
    --front-dark: #5f5d59;
    --front-mid: #8d8984;
    --front-light: #d9d3cc;
    --back-light: #b3aba4;
    --back-dark: #6f6963;
    --brand-dark: #2c2520;
    --brand-light: #efe7df;
    --text-light: #f4eee8;
  }
  * { margin: 0; padding: 0; box-sizing: border-box; }
  html, body { width: 1200px; height: 800px; overflow: hidden; background: var(--page); }
  .canvas { position: relative; width: 1200px; height: 800px; }

  .card {
    position: absolute;
    top: 262px;
    width: 432px;
    height: 246px;
    box-shadow: 0 10px 24px rgba(60, 50, 40, 0.18);
  }
  .card--front { left: 136px; }
  .card--back { left: 636px; width: 430px; }

  .front-texture {
    position: absolute; inset: 0;
    background: radial-gradient(ellipse at 68% 78%, var(--front-light) 0%, var(--front-mid) 45%, var(--front-dark) 100%);
  }
  .brand {
    position: absolute;
    display: flex; flex-direction: column; align-items: center;
    font-family: "Montserrat", sans-serif;
    font-weight: 600;
    text-align: center;
  }
  .brand__mark { width: 40px; height: 40px; margin-bottom: 14px; }
  .brand__name { font-size: 15px; letter-spacing: 2.5px; line-height: 1; }
  .brand__sub { font-size: 8px; letter-spacing: 2px; margin-top: 8px; }

  .card--front .brand { left: 0; right: 0; top: 66px; color: var(--brand-dark); }
  .card--front .brand__mark { background: var(--brand-dark); }

  .card--back {
    background: radial-gradient(ellipse at 45% 10%, var(--back-light) 0%, #958d86 50%, var(--back-dark) 100%);
  }
  .card--back .brand { left: 30px; width: 190px; top: 66px; color: var(--brand-light); }
  .card--back .brand__mark { border: 2px solid var(--brand-light); }

  .contact { position: absolute; left: 206px; top: 40px; font-family: "Roboto", sans-serif; color: var(--text-light); }
  .contact__name { font-size: 21px; font-weight: 500; margin-left: 4px; margin-bottom: 22px; text-shadow: 0 1px 1px rgba(0,0,0,0.25); }
  .contact__list { list-style: none; }
  .contact__item { display: flex; align-items: center; gap: 12px; height: 22px; margin-bottom: 22px; font-size: 12px; }
  .contact__icon { width: 22px; height: 22px; flex: none; }
</style>
</head>
<body>
<main class="canvas">

  <section class="card card--front">
    <div class="front-texture" role="img" aria-label="Fine diagonal herringbone line pattern in warm greys"></div>
    <div class="brand">
      <span class="brand__mark"></span>
      <span class="brand__name">STONEHAVEN</span>
      <span class="brand__sub">CUSTOM BUILDERS</span>
    </div>
  </section>

  <section class="card card--back">
    <div class="brand">
      <span class="brand__mark"></span>
      <span class="brand__name">STONEHAVEN</span>
      <span class="brand__sub">CUSTOM BUILDERS</span>
    </div>

    <div class="contact">
      <h1 class="contact__name">Colin Marsh</h1>
      <ul class="contact__list">
        <li class="contact__item">
          <svg class="contact__icon" viewBox="0 0 24 24" aria-hidden="true">
            <path fill="#f4eee8" d="M6.6 3.5l3 3.2-1.8 2.4c1.2 2.6 3.3 4.7 5.9 5.9l2.4-1.8 3.2 3-1.6 3.2c-7.8-.6-13.4-6.2-14-14z"/>
          </svg>
          <span>208 637 4120</span>
        </li>
        <li class="contact__item">
          <svg class="contact__icon" viewBox="0 0 24 24" aria-hidden="true">
            <rect x="2" y="5" width="20" height="14" fill="#f4eee8"/>
            <path d="M2 5l10 8 10-8" fill="none" stroke="#7d766f" stroke-width="1.5"/>
          </svg>
          <span>ColinMarshSCB@quillpost.net</span>
        </li>
        <li class="contact__item">
          <svg class="contact__icon" viewBox="0 0 24 24" aria-hidden="true">
            <circle cx="12" cy="12" r="10" fill="#f4eee8"/>
            <g fill="none" stroke="#7d766f" stroke-width="1.2">
              <ellipse cx="12" cy="12" rx="4.5" ry="10"/>
              <path d="M2 12h20M4 7h16M4 17h16"/>
            </g>
          </svg>
          <span>Stonehavencustombuilders.com</span>
        </li>
      </ul>
    </div>
  </section>

</main>
</body>
</html>
```